Business card and stationary for a consultant firm
Sharp Compass
Professional
Renske Hoorneman
Zwaluwlaan 38
Curaçao
Renskehoorneman@postvlek.com
Zwaluwlaan38

```html
<!DOCTYPE html>
<html lang="en">
<head>
<meta charset="utf-8">
<title>Sharp Compass – Business Card</title>
<link rel="stylesheet" href="https://fonts.googleapis.com/css2?family=Crimson+Pro:wght@400;600;700&display=swap">
<style>
  :root {
    --backdrop: #e9e7e3;
    --card: #ffffff;
    --ink: #1d1d1b;
    --muted: #8a8a8a;
    --rule: #9a9a9a;
    --band-light: #8fc03e;
    --band-mid: #2f7fa8;
    --band-dark: #151515;
    --mark: #2fa6c9;
    --icon: #555555;
  }
  * { margin: 0; padding: 0; box-sizing: border-box; }
  html, body {
    width: 1200px;
    height: 778px;
    overflow: hidden;
    background: var(--backdrop);
  }
  .canvas {
    position: relative;
    width: 1200px;
    height: 778px;
  }
  .card {
    position: absolute;
    left: 165px;
    top: 144px;
    width: 870px;
    height: 490px;
    border-radius: 30px;
    background: var(--card);
    overflow: hidden;
    box-shadow: 0 6px 18px rgba(0,0,0,0.18);
    font-family: "Crimson Pro", Georgia, serif;
    color: var(--ink);
  }
  .card__band {
    position: absolute;
    inset: 0;
    width: 870px;
    height: 490px;
  }
  .brand {
    position: absolute;
    left: 62px;
    top: 52px;
    display: flex;
    align-items: center;
  }
  .brand__dot {
    width: 72px;
    height: 72px;
    border-radius: 50%;
    background: var(--mark);
  }
  .brand__rule {
    width: 2px;
    height: 96px;
    background: var(--rule);
    margin: 0 16px 0 20px;
  }
  .brand__name {
    font-size: 50px;
    font-weight: 600;
    color: var(--ink);
  }
  .contact {
    position: absolute;
    left: 60px;
    top: 290px;
    font-size: 25px;
    line-height: 36px;
  }
  .contact__line {
    display: flex;
    align-items: center;
  }
  .contact__icon {
    width: 20px;
    height: 20px;
    margin-right: 12px;
    flex: none;
  }
  .person {
    position: absolute;
    left: 588px;
    top: 258px;
    transform: rotate(-40deg);
    transform-origin: left bottom;
    white-space: nowrap;
  }
  .person__name {
    font-size: 29px;
    font-weight: 700;
    line-height: 1;
  }
  .person__role {
    position: absolute;
    top: 100%;
    left: 26px;
    font-size: 22px;
    line-height: 1.1;
    color: var(--muted);
  }
</style>
</head>
<body>
<div class="canvas">
  <div class="card">
    <svg class="card__band" viewBox="0 0 870 490" role="img" aria-label="Diagonal colour band in the lower right corner">
      <defs>
        <linearGradient id="bandFill" x1="560" y1="330" x2="760" y2="500" gradientUnits="userSpaceOnUse">
          <stop offset="0" stop-color="var(--band-light)"/>
          <stop offset="0.45" stop-color="var(--band-mid)"/>
          <stop offset="1" stop-color="var(--band-dark)"/>
        </linearGradient>
      </defs>
      <polygon fill="url(#bandFill)" points="458,490 870,146 870,490"/>
    </svg>

    <div class="brand">
      <div class="brand__dot"></div>
      <div class="brand__rule"></div>
      <div class="brand__name">Sharpcompass</div>
    </div>

    <div class="person">
      <div class="person__name">Renske Hoorneman</div>
      <div class="person__role">Managing Director</div>
    </div>

    <div class="contact">
      <div class="contact__line">Zwaluwlaan 38</div>
      <div class="contact__line">Curaçao</div>
      <div class="contact__line">
        <svg class="contact__icon" viewBox="0 0 20 20" aria-hidden="true">
          <rect x="6" y="2" width="8" height="16" rx="1.5" fill="none" stroke="var(--icon)" stroke-width="1.6"/>
          <rect x="8" y="4.5" width="4" height="5" fill="var(--icon)"/>
        </svg>
        (599-9) 7240518
      </div>
      <div class="contact__line">
        <svg class="contact__icon" viewBox="0 0 20 20" aria-hidden="true">
          <rect x="2" y="5" width="16" height="11" fill="none" stroke="var(--icon)" stroke-width="1.6"/>
          <polyline points="2,5 10,11.5 18,5" fill="none" stroke="var(--icon)" stroke-width="1.6"/>
        </svg>
        Renskehoorneman@postvlek.com
      </div>
    </div>
  </div>
</div>
</body>
</html>
```